I need an advertisement graphic made in two different sizes for a golf tournament

I need an ad made in two different sizes, but can be similar, for a golf tournament

The key components are:

See the future stars of the LKR CIRCUIT at the

Fennwick Bay Classic (logo attached)

May 21-24 at Marrowdale Pines Country Club

Admission is free for everyone!

I need it in the following sizes
1302px wide X 1085 px tall
3840px wide x 2160px tall

I have also added a picture of the golf course
If you use colors, stick with the color scheme in the logo

```html
<!DOCTYPE html>
<html lang="en">
<head>
<meta charset="utf-8">
<title>Fennwick Bay Classic – Ad Set</title>
<link href="https://fonts.googleapis.com/css2?family=Oswald:wght@500;700&family=Montserrat:wght@600;800&display=swap" rel="stylesheet">
<style>
  :root {
    --navy: #213f57;
    --green: #97c354;
    --white: #ffffff;
    --stage: #ababab;
    --sky-top: #b9d9f1;
    --sky-haze: #f3f8fb;
    --hill: #3f6b2c;
    --fairway: #8fbf2e;
    --fairway-light: #c7da3c;
  }
  * { box-sizing: border-box; margin: 0; padding: 0; }
  html, body {
    width: 932px; height: 1200px; overflow: hidden;
    background: var(--stage);
  }
  .ad {
    position: absolute; overflow: hidden;
    box-shadow: 6px 8px 14px rgba(0,0,0,0.28);
  }
  .ad--square { left: 186px; top: 114px; width: 561px; height: 468px; }
  .ad--wide { left: 49px; top: 607px; width: 833px; height: 468px; }

  .course-photo {
    position: absolute; inset: 0;
    background: linear-gradient(180deg, var(--sky-top) 0%, var(--sky-haze) 30%, #eef5f9 46%, var(--hill) 49%, #5d8f2f 58%, var(--fairway) 74%, var(--fairway-light) 100%);
  }
  .ad--wide .course-photo {
    background: linear-gradient(180deg, var(--sky-top) 0%, var(--sky-haze) 30%, #eef5f9 50%, var(--hill) 53%, #5d8f2f 62%, var(--fairway) 78%, var(--fairway-light) 100%);
  }
  .panel { position: absolute; inset: 0; width: 100%; height: 100%; }

  .event-name {
    position: absolute; text-align: center; color: var(--navy);
    font-family: "Oswald", sans-serif; font-weight: 700; text-transform: uppercase;
  }
  .event-name__tagline {
    display: block; font-weight: 500; font-size: 15px; letter-spacing: 0.06em; margin-bottom: 4px;
  }
  .event-name__title { display: block; font-size: 58px; line-height: 1.0; letter-spacing: 0.01em; }
  .ad--square .event-name { left: 100px; width: 370px; top: 42px; }
  .ad--wide .event-name { left: 30px; width: 380px; top: 92px; }

  .badge {
    position: absolute; width: 168px; height: 168px; border-radius: 50%;
    background: var(--green); color: var(--navy);
    box-shadow: 2px 6px 12px rgba(0,0,0,0.3);
    display: flex; flex-direction: column; align-items: center; justify-content: center;
    font-family: "Oswald", sans-serif; text-transform: uppercase; line-height: 1;
  }
  .ad--square .badge { left: 364px; top: 279px; }
  .ad--wide .badge { left: 376px; top: 206px; }
  .badge__lead { font-weight: 500; font-size: 21px; letter-spacing: 0.01em; }
  .badge__free { font-weight: 700; font-size: 64px; letter-spacing: 0.01em; margin: 2px 0 3px; }
  .badge__tail { font-weight: 500; font-size: 16px; }

  .dates {
    position: absolute; color: var(--white);
    font-family: "Montserrat", sans-serif; font-weight: 800; line-height: 1; letter-spacing: -0.01em;
  }
  .venue {
    position: absolute; color: var(--green);
    font-family: "Montserrat", sans-serif; font-weight: 600; text-transform: uppercase; line-height: 1.2;
  }
  .ad--square .dates { left: 45px; top: 374px; font-size: 52px; }
  .ad--square .venue { left: 45px; top: 428px; font-size: 14.5px; }
  .ad--wide .dates { left: 566px; top: 118px; font-size: 90px; line-height: 0.82; }
  .ad--wide .venue { left: 566px; top: 286px; font-size: 24px; line-height: 1.35; }
  .website {
    position: absolute; right: 45px; top: 398px; color: var(--white);
    font-family: "Montserrat", sans-serif; font-weight: 600; font-size: 22px;
  }
</style>
</head>
<body>

<section class="ad ad--square">
  <div class="course-photo" role="img" aria-label="Aerial photo of a tree-lined golf fairway with bunkers, wooded hills and a bright sky"></div>
  <svg class="panel" viewBox="0 0 561 468" aria-hidden="true">
    <path d="M0 310 Q200 372 561 394 L561 406 Q200 384 0 322 Z" fill="var(--green)"/>
    <path d="M0 322 Q200 384 561 406 L561 468 L0 468 Z" fill="var(--navy)"/>
  </svg>
  <h1 class="event-name">
    <span class="event-name__tagline">See the future stars of the LKR Circuit</span>
    <span class="event-name__title">Fennwick Bay<br>Classic</span>
  </h1>
  <p class="dates">MAY 21-24</p>
  <p class="venue">Marrowdale Pines Country Club</p>
  <div class="badge">
    <span class="badge__lead">Admission is</span>
    <span class="badge__free">Free</span>
    <span class="badge__tail">For everyone!</span>
  </div>
</section>

<section class="ad ad--wide">
  <div class="course-photo" role="img" aria-label="Aerial photo of a tree-lined golf fairway with bunkers, wooded hills and a bright sky"></div>
  <svg class="panel" viewBox="0 0 833 468" aria-hidden="true">
    <path d="M494 0 Q450 210 428 468 L442 468 Q462 214 506 0 Z" fill="var(--green)"/>
    <path d="M506 0 Q462 214 442 468 L833 468 L833 0 Z" fill="var(--navy)"/>
  </svg>
  <h1 class="event-name">
    <span class="event-name__tagline">See the future stars of the LKR Circuit</span>
    <span class="event-name__title">Fennwick Bay<br>Classic</span>
  </h1>
  <p class="dates">MAY<br>21-24</p>
  <p class="venue">Marrowdale Pines<br>Country Club</p>
  <p class="website">www.fennwickbayclassic.com</p>
  <div class="badge">
    <span class="badge__lead">Admission is</span>
    <span class="badge__free">Free</span>
    <span class="badge__tail">For everyone!</span>
  </div>
</section>

</body>
</html>
```